Real Estate investment company needs billboard designs

This is our website: https://velmarkpropertygroup.com/
We are looking for some billboard concepts that uses our CEO in the design. I have attached some images and 1 billboard design that someone in our industry uses, but we don't want it exactly like his.

Industry/Entity Type

real estate

Colors

Designer to choose colors to be used in the design.

Requirements
Must have
• Company colors from websiute

```html
<!DOCTYPE html>
<html lang="en">
<head>
<meta charset="utf-8">
<title>Velmark Property Group — Sell Your Home Billboard</title>
<link rel="stylesheet" href="https://fonts.googleapis.com/css2?family=Anton&family=Oswald:wght@500;600&family=Tinos:wght@700&display=swap">
<style>
  :root {
    --bg-dark: #2b2d30;
    --bg-mid: #3b3e42;
    --gold: #e0bd8c;
    --gold-deep: #c9a06a;
    --white: #ffffff;
    --soft: #d9dadb;
    --rule: #c9b08f;
  }
  * { margin: 0; padding: 0; box-sizing: border-box; }
  html, body { width: 1200px; height: 601px; overflow: hidden; background: var(--bg-dark); }
  .billboard { position: relative; width: 1200px; height: 601px; overflow: hidden; }
  .billboard-art { position: absolute; inset: 0; }

  .brand {
    position: absolute; left: 60px; top: 40px;
    display: flex; align-items: center; gap: 12px;
    font-family: "Oswald", sans-serif; font-weight: 600; font-size: 22px;
    letter-spacing: 3px; text-transform: uppercase; color: var(--white); line-height: 1;
  }
  .brand-dot { width: 16px; height: 16px; border-radius: 50%; background: var(--gold); }

  .headline {
    position: absolute; left: 58px; top: 96px;
    font-family: "Anton", sans-serif; font-weight: 400; font-size: 76px;
    color: var(--white); letter-spacing: 1px; line-height: 1.1; white-space: nowrap;
  }
  .subline {
    position: absolute; left: 60px; top: 196px;
    font-family: "Oswald", sans-serif; font-weight: 500; font-size: 18px;
    letter-spacing: 1px; color: var(--gold); text-transform: uppercase; white-space: nowrap;
  }
  .subline .divider { display: inline-block; width: 1px; height: 15px; background: var(--gold); margin: 0 12px; vertical-align: -1px; }

  .offer, .call { position: absolute; left: 60px; font-family: "Tinos", serif; font-weight: 700; }
  .offer { top: 262px; padding-left: 14px; border-left: 2px solid var(--rule); font-size: 22px; line-height: 1.4; }
  .offer .accent { display: block; color: var(--gold); }
  .offer .plain { display: block; color: var(--white); }

  .call { top: 420px; padding-left: 14px; border-left: 2px solid var(--rule); line-height: 1.25; }
  .call-label { display: block; color: var(--gold); font-size: 24px; }
  .call-phone { display: block; color: var(--white); font-size: 46px; letter-spacing: 1px; }
  .call-note { display: block; color: var(--soft); font-size: 20px; }
</style>
</head>
<body>
<main class="billboard">
  <svg class="billboard-art" width="1200" height="601" viewBox="0 0 1200 601">
    <defs>
      <linearGradient id="house-tone" x1="0" y1="0" x2="0" y2="1">
        <stop offset="0" stop-color="#c9ced3"/>
        <stop offset="0.55" stop-color="#e9ebec"/>
        <stop offset="0.8" stop-color="#6f8f48"/>
        <stop offset="1" stop-color="#7fa64a"/>
      </linearGradient>
      <linearGradient id="family-tone" x1="0" y1="0" x2="0" y2="1">
        <stop offset="0" stop-color="#f2efea"/>
        <stop offset="1" stop-color="#d8cfc2"/>
      </linearGradient>
      <linearGradient id="ceo-tone" x1="0" y1="0" x2="0" y2="1">
        <stop offset="0" stop-color="#8c96a3"/>
        <stop offset="1" stop-color="#2f3a4a"/>
      </linearGradient>
    </defs>

    <rect width="1200" height="601" fill="var(--bg-dark)"/>
    <polygon points="0,601 0,470 560,601" fill="var(--bg-mid)"/>

    <polygon class="photo-house" points="770,0 1200,0 1200,601 640,601" fill="url(#house-tone)" role="img" aria-label="Photo of a white single-story house with dark shutters and a green lawn"/>
    <line x1="770" y1="0" x2="640" y2="601" stroke="var(--gold)" stroke-width="6"/>

    <path class="photo-ceo" d="M 830 601 V 250 A 150 150 0 0 1 1130 250 V 601 Z" fill="url(#ceo-tone)" stroke="var(--gold)" stroke-width="6" role="img" aria-label="Portrait of the company CEO in business attire, smiling"/>

    <circle class="photo-family" cx="700" cy="120" r="72" fill="url(#family-tone)" stroke="var(--white)" stroke-width="5" role="img" aria-label="Photo of a happy family relaxing on a sofa at home"/>
  </svg>

  <div class="brand"><span class="brand-dot"></span>Velmark Property Group</div>

  <h1 class="headline">SELL YOUR HOME</h1>
  <p class="subline">Get your cash offer<span class="divider"></span>Sell your house fast</p>

  <p class="offer">
    <span class="accent">Get Your</span>
    <span class="accent">FREE Offer.</span>
    <span class="plain">Same Day,</span>
    <span class="plain">No Obligations, Just Options.</span>
  </p>

  <p class="call">
    <span class="call-label">Call Now</span>
    <span class="call-phone">865-555-0142</span>
    <span class="call-note">Get a Cash Offer, Same Day</span>
  </p>
</main>
</body>
</html>
```